design an app for runners to engage them in collective challenges

Creative Brief: Running Application - Collective Challenges
Objective
To design a simple yet impactful mobile application for runners, centered around collective challenges. The app should offer an engaging, user-friendly experience while encouraging participation in running challenges. Starting with a minimalist and robust version, the design must focus on essential features, allowing for future enhancements as the user base grows.

Target Audience
Primary Users: Casual to dedicated runners who enjoy tracking their progress and participating in challenges.
Motivations: Community-driven goals, personal achievements, and tangible rewards.
Needs: A visually appealing, straightforward interface with real-time progress tracking and clear challenge objectives.
Core Features
Main Screen: Current Challenge

Displays the active challenge with a title, visual, prize description, and countdown for kilometers remaining.
Prominent “Join” button for easy participation.
Quick access to challenge conditions (eg, most kilometers, fastest pace, random draw).
Challenge Details

Includes challenge rules, detailed prize information, and victory conditions.
Simplified text for clarity and engagement.
Past Challenges

Showcases previous challenges, total kilometers achieved, and winners.
Admin Section

Enables challenge creation with scheduling, descriptions, and victory criteria.
Minimalist design for ease of use.
Look and Feel
Visual Identity: Clean, modern, and energetic design reflecting the spirit of running and collective achievement.
Color Palette:
Vibrant primary colors: Blue and green for energy and motivation.
Accent colors: Orange or yellow for highlights, paired with a dark background for strong contrast.
Typography:
Sans-serif fonts like Lato or Montserrat for readability.
Bold, prominent numbers for key statistics like kilometers completed.
Icons and Graphics:
Minimalistic icons with light, functional animations (eg, a moving kilometer counter).
Clear, motivational visuals to support collective progress.
Tone and Style
Tone: Encouraging, community-focused, and goal-oriented.
Style: Minimalistic with a focus on clarity and user engagement.
References
Inspirations:
Tavro Stride Circle for its simplicity and modern interface.
Pellux for its community features and tracking precision.
Deliverables
Wireframes and UI designs for all key screens: login, current challenge, challenge details, past challenges, and admin panel.
Visual assets: icons, buttons, and animations.
A consistent design system to ensure scalability for future features.
Updates

Target Market(s)

Casual to dedicated runners who enjoy tracking their progress and participating in challenges.

Industry/Entity Type

sport

Font styles to use
Sans Serif

Colors

Designer to choose colors to be used in the design.

Requirements
Must have
• to design all screens

```html
<!DOCTYPE html>
<html lang="en">
<head>
<meta charset="utf-8">
<title>Running Challenges App Screens</title>
<link href="https://fonts.googleapis.com/css2?family=Montserrat:wght@400;500;600;700;800&display=swap" rel="stylesheet">
<style>
:root{
  --stage:#2563e6;
  --ink:#141a25;
  --card:#3a3d45;
  --card-dark:#2c2f36;
  --field:#2f3238;
  --blue:#1f7cf2;
  --blue-light:#3d94ff;
  --blue-tile:#2f80f2;
  --green:#22c55e;
  --green-dark:#16a34a;
  --pill:#14532d;
  --gold:#f5c518;
  --red:#e23d4b;
  --nav:#eceef1;
  --nav-icon:#8d939c;
  --white:#ffffff;
}
*{box-sizing:border-box;margin:0;padding:0}
html,body{width:1200px;height:1200px;overflow:hidden}
body{background:var(--stage);font-family:'Montserrat',sans-serif;color:var(--white);position:relative}
.screen{position:absolute;width:216px;height:478px;background:var(--ink);border-radius:28px;overflow:hidden}
.s-home{left:117px;top:66px}
.s-home2{left:490px;top:66px}
.s-stats{left:834px;top:66px}
.s-join{left:117px;top:662px}
.s-create{left:490px;top:662px}
.s-signup{left:834px;top:662px}

.welcome{display:flex;align-items:center;padding:40px 12px 0 12px;gap:5px}
.avatar{width:26px;height:26px;border-radius:50%;background:var(--blue);font-size:8px;font-weight:700;display:flex;align-items:center;justify-content:center}
.welcome .who{flex:1;line-height:1.1}
.welcome .who small{display:block;font-size:6.5px;font-weight:500}
.welcome .who b{font-size:8.5px;font-weight:700}
.bell{width:16px;height:16px}

.topbar{background:var(--blue);height:64px;padding:38px 10px 0;display:flex;align-items:flex-start;gap:8px;font-size:8.5px;font-weight:500}
.topbar .back{width:12px;height:12px;margin-top:-1px}
.topbar .join-btn{margin-left:auto;margin-top:-7px;background:var(--blue-light);border-radius:8px;padding:5px 14px;font-size:8.5px;box-shadow:0 1px 2px rgba(0,0,0,.2)}

.hero{position:relative;margin:12px 10px 0;height:148px;border-radius:8px;background:linear-gradient(135deg,#4299ff,#1e72ea);overflow:hidden;text-align:center}
.hero::after{content:"";position:absolute;width:170px;height:170px;border-radius:50%;background:rgba(255,255,255,.09);right:-70px;top:-28px}
.hero .runner{width:30px;height:34px;margin-top:20px}
.hero .big{font-size:20px;font-weight:800;line-height:1;margin-top:4px}
.hero .label{font-size:8px;letter-spacing:1.6px;font-weight:500}
.crown{position:absolute;width:18px;height:14px;right:13px;top:11px}
.tiles{position:absolute;left:7px;right:7px;bottom:6px;display:flex;gap:8px;z-index:1}
.tile{flex:1;height:36px;border-radius:6px;background:var(--blue-tile);font-size:8px;line-height:1.25;display:flex;flex-direction:column;justify-content:center;text-align:center}
.tile span{font-weight:400;opacity:.9}
.tile b{font-weight:600}
.tile svg{width:9px;height:9px;margin:0 auto 1px}

.section{font-size:7px;font-weight:700;padding:14px 20px 6px}
.section.lg{font-size:8.5px;padding:10px 20px 5px}

.challenge{position:relative;margin:0 10px;border-radius:6px;background:linear-gradient(180deg,#50535b 0%,#383b42 55%,#2c2f35 100%);padding:10px 10px 8px}
.challenge h3{font-size:10.5px;font-weight:700;line-height:1.1}
.challenge .sub{font-size:6.5px;color:#dde0e6}
.pill{position:absolute;right:10px;top:-8px;background:var(--pill);color:var(--green);border:1.5px solid #d8f5e3;border-radius:9px;font-size:7.5px;padding:2px 8px}
.progress-row{display:flex;justify-content:space-between;font-size:6.5px;margin-top:9px}
.bar{height:4px;border-radius:2px;background:#2a2d33;margin-top:6px}
.bar i{display:block;height:100%;width:57%;border-radius:2px;background:var(--green)}
.prize{display:flex;align-items:center;gap:7px;background:var(--green-dark);border-radius:3px;margin-top:13px;padding:5px 9px;font-size:8px}
.prize b{margin-left:auto;font-weight:700}
.prize svg{width:9px;height:9px}

.activity{display:flex;align-items:center;margin:0 10px 6px;background:var(--card);border-radius:3px;padding:5px 12px;height:27px}
.activity div{flex:1;line-height:1.15}
.activity b{font-size:8px;font-weight:600;display:block}
.activity small{font-size:6.5px}
.activity svg{width:7px;height:8px}

.result{display:flex;align-items:center;margin:0 10px 7px;background:var(--card-dark);border-radius:4px;padding:0 12px;height:32px}
.result div{flex:1;line-height:1.2}
.result b{font-size:8px;font-weight:600;display:block}
.result small{font-size:6.5px;color:#d0d4da}
.medal{width:10px;height:12px}

.history{position:relative;margin:0 12px 6px;background:var(--card);border-radius:4px;padding:7px 10px;height:42px;line-height:1.3}
.history b{font-size:8px;font-weight:600;display:block}
.history small{display:block;font-size:6.5px;color:#d8dbe0}
.history .medal{position:absolute;right:10px;top:8px}
.history .chev{position:absolute;right:10px;bottom:7px;width:6px;height:7px}

.nav{position:absolute;left:0;right:0;bottom:0;height:36px;background:var(--nav);display:flex;justify-content:space-around;align-items:center;padding:0 18px;z-index:2}
.nav svg{width:12px;height:12px;color:var(--nav-icon)}
.nav svg.on{color:var(--blue)}

.active-tag{position:absolute;right:5px;top:6px;background:var(--blue);border-radius:8px;font-size:8px;padding:3px 7px;z-index:1}
.progress-card{margin:9px 10px 0;border-radius:6px;background:linear-gradient(180deg,#50535b,#34373d);padding:7px 12px 6px}
.progress-card h3{font-size:10.5px;font-weight:700}
.metrics{display:flex;justify-content:space-between;font-size:8px;margin-top:7px;line-height:1.1}
.metrics div:nth-child(2){text-align:center}
.metrics div:last-child{text-align:right}
.metrics b{font-weight:600}
.rules{margin:9px 9px 0;background:var(--card);border-radius:6px;padding:8px 8px 4px}
.rule{display:flex;gap:12px;align-items:center;margin-bottom:5px;line-height:1.1}
.rule svg{width:11px;height:11px;flex:none}
.rule b{font-size:8px;font-weight:600;display:block}
.rule small{font-size:6.5px}
.place{display:flex;align-items:center;gap:8px;margin:10px 12px 0;background:var(--card);border-radius:4px;padding:6px 10px;font-size:8px}
.place b{margin-left:auto;font-weight:500}

.form{padding:0 10px}
.form label{display:block;font-size:8px;font-weight:600;line-height:10px;margin:8px 0 4px}
.input{height:28px;border-radius:4px;background:var(--field);border:1px solid #3e4148;font-size:8px;color:#c9ccd2;padding:0 10px;display:flex;align-items:center}
.input.area{height:60px;align-items:flex-start;padding-top:9px}
.upload{height:60px;border:1px dashed #3f434a;border-radius:4px;text-align:center;padding-top:20px;line-height:1.2}
.upload b{font-size:8px;color:#8d929a;font-weight:600;display:block}
.upload small{font-size:6.5px;color:#777c84}
.input .trash{margin-left:auto;width:9px;height:10px}
.add-rule{height:27px;border:1px dashed #3f434a;border-radius:4px;margin-top:5px;font-size:8px;color:#7d828a;display:flex;align-items:center;justify-content:center}
.primary{position:absolute;left:10px;right:10px;bottom:12px;height:36px;background:var(--blue);border-radius:4px;font-size:8.5px;font-weight:500;display:flex;align-items:center;justify-content:center}

.photo{height:184px;background:linear-gradient(180deg,#9a7a68 0%,#6e5a4f 35%,#3b3836 70%,#24252a 100%)}
.signup-head{text-align:center;margin-top:9px}
.signup-head h2{font-size:11px;font-weight:700;line-height:14px}
.signup-head p{font-size:5.5px;line-height:7px;margin-top:4px}
.s-signup .form label{margin:6px 0 4px}
.s-signup .form label:first-child{margin-top:14px}
.s-signup .primary{bottom:16px}
</style>
</head>
<body>

<svg width="0" height="0" style="position:absolute">
  <defs>
    <symbol id="i-home" viewBox="0 0 24 24"><path fill="currentColor" d="M12 3 2 11.5h3V21h5.5v-6h3v6H19v-9.5h3z"/></symbol>
    <symbol id="i-trophy" viewBox="0 0 24 24"><path fill="currentColor" d="M6 3h12v2h3v3a4 4 0 0 1-4 4h-.4A5 5 0 0 1 13 15v3h4v3H7v-3h4v-3a5 5 0 0 1-3.6-3H7a4 4 0 0 1-4-4V5h3zM5 7v1a2 2 0 0 0 1.6 2L6 7zm14 0h-1l-.6 3A2 2 0 0 0 19 8z"/></symbol>
    <symbol id="i-history" viewBox="0 0 24 24"><path fill="none" stroke="currentColor" stroke-width="2.2" stroke-linecap="round" d="M4 12a8 8 0 1 0 2.3-5.6M4 4v4h4M12 8v4.5l3 2"/></symbol>
    <symbol id="i-user" viewBox="0 0 24 24"><circle cx="12" cy="7.5" r="4.5" fill="currentColor"/><path fill="currentColor" d="M3 21c0-5 4-7.5 9-7.5s9 2.5 9 7.5z"/></symbol>
    <symbol id="i-chev" viewBox="0 0 8 10"><path d="M2 1l4 4-4 4" fill="none" stroke="currentColor" stroke-width="1.8"/></symbol>
    <symbol id="i-back" viewBox="0 0 14 14"><path d="M13 7H2M7 2 2 7l5 5" fill="none" stroke="currentColor" stroke-width="1.8" stroke-linecap="round"/></symbol>
    <symbol id="i-bell" viewBox="0 0 24 24"><path d="M6 17V11a6 6 0 0 1 12 0v6l2 2H4zM10 21h4M12 3v2" fill="none" stroke="currentColor" stroke-width="1.8" stroke-linejoin="round"/></symbol>
    <symbol id="i-crown" viewBox="0 0 24 18"><path d="M2 4l5 6 5-8 5 8 5-6-2 11H4zM4 17h16" fill="none" stroke="currentColor" stroke-width="1.6" stroke-linejoin="round"/></symbol>
    <symbol id="i-runner" viewBox="0 0 30 34"><circle cx="19" cy="4" r="3.5" fill="currentColor"/><path d="M8 12l6-3 5 1 3 6 5 1M16 10l-3 9 6 4-2 9M13 19l-4 6-7 0" fill="none" stroke="currentColor" stroke-width="3.4" stroke-linecap="round" stroke-linejoin="round"/></symbol>
    <symbol id="i-medal" viewBox="0 0 10 12"><circle cx="5" cy="4" r="3.2" fill="none" stroke="currentColor" stroke-width="1.6"/><path d="M3 6.8 2 11l3-1.5L8 11 7 6.8" fill="currentColor"/></symbol>
    <symbol id="i-cup" viewBox="0 0 10 10"><path d="M1 1h8v2.5a4 4 0 0 1-8 0zM2.5 7.5 1 9.5M7.5 7.5 9 9.5" fill="none" stroke="currentColor" stroke-width="1.5"/></symbol>
    <symbol id="i-cal" viewBox="0 0 12 12"><rect x="1" y="2" width="10" height="9" rx="1" fill="currentColor"/><path d="M3.5 0.5v3M8.5 0.5v3" stroke="currentColor" stroke-width="1.4"/><rect x="2" y="5" width="8" height="5" fill="#3a3d45" opacity=".35"/></symbol>
    <symbol id="i-trash" viewBox="0 0 10 11"><path d="M1 2.5h8M3.5 2.5V1h3v1.5M2 2.5l.6 8h4.8l.6-8M4 4.5v4M6 4.5v4" fill="none" stroke="currentColor" stroke-width="1"/></symbol>
  </defs>
</svg>

<!-- Home: today's progress -->
<section class="screen s-home">
  <header class="welcome">
    <div class="avatar">TM</div>
    <div class="who"><small>Welcome Back</small><b>Tom M.</b></div>
    <svg class="bell"><use href="#i-bell"/></svg>
  </header>
  <div class="hero">
    <svg class="crown" style="color:var(--gold)"><use href="#i-crown"/></svg>
    <svg class="runner"><use href="#i-runner"/></svg>
    <div class="big">2.5 km</div>
    <div class="label">Today's Progress</div>
    <div class="tiles">
      <div class="tile"><span>Time</span><b>22 Min</b></div>
      <div class="tile"><span>Pace</span><b>8'48" /km</b></div>
      <div class="tile"><span>Calories</span><b>186 kcal</b></div>
    </div>
  </div>
  <div class="section">Current Challenge</div>
  <div class="challenge">
    <span class="pill">Active</span>
    <h3>100km Challenge</h3>
    <div class="sub">12 days remaining</div>
    <div class="progress-row"><span>35.8 km completed</span><span>53%</span></div>
    <div class="bar"><i></i></div>
    <div class="prize"><svg><use href="#i-medal"/></svg><span>Prize Pool</span><b>US. 10,000</b></div>
  </div>
  <div class="section lg">Recent Activities</div>
  <div class="activity"><div><b>Today · 6:30 AM</b><small>2.5 km &nbsp;22 min</small></div><svg><use href="#i-chev"/></svg></div>
  <div class="activity" style="margin-top:8px"><div><b>Yesterday · 6:15 AM</b><small>2.5 km &nbsp;22 min</small></div><svg><use href="#i-chev"/></svg></div>
  <nav class="nav"><svg class="on"><use href="#i-home"/></svg><svg><use href="#i-trophy"/></svg><svg><use href="#i-history"/></svg><svg><use href="#i-user"/></svg></nav>
</section>

<!-- Home: challenge and results -->
<section class="screen s-home2">
  <header class="welcome">
    <div class="avatar">TM</div>
    <div class="who"><small>Welcome Back</small><b>Tom M.</b></div>
    <svg class="bell"><use href="#i-bell"/></svg>
  </header>
  <div class="section" style="padding-top:18px">Current Challenge</div>
  <div class="challenge">
    <span class="pill">Active</span>
    <h3>100km Challenge</h3>
    <div class="sub">12 days remaining</div>
    <div class="progress-row"><span>35.8 km completed</span><span>53%</span></div>
    <div class="bar"><i></i></div>
    <div class="prize"><svg><use href="#i-medal"/></svg><span>Prize Pool</span><b>US. 10,000</b></div>
  </div>
  <div class="section lg" style="padding-top:12px">Recent Activities</div>
  <div class="activity"><div><b>Today · 6:30 AM</b><small>2.5 km &nbsp;22 min</small></div><svg><use href="#i-chev"/></svg></div>
  <div class="activity"><div><b>Yesterday · 6:15 AM</b><small>2.5 km &nbsp;22 min</small></div><svg><use href="#i-chev"/></svg></div>
  <div class="section lg" style="padding-top:5px">Recent Activities</div>
  <div class="result"><div><b>50km Speed Run</b><small>Completed · Won 2nd Place</small></div><svg class="medal" style="color:#c7c316"><use href="#i-medal"/></svg></div>
  <div class="result"><div><b>Marathon Prep</b><small>Completed · Participation</small></div><svg class="medal"><use href="#i-medal"/></svg></div>
  <nav class="nav"><svg class="on"><use href="#i-home"/></svg><svg><use href="#i-trophy"/></svg><svg><use href="#i-history"/></svg><svg><use href="#i-user"/></svg></nav>
</section>

<!-- Overall statistics -->
<section class="screen s-stats">
  <header class="topbar"><svg class="back"><use href="#i-back"/></svg><span>Overall Statistics</span></header>
  <div class="hero" style="height:84px;text-align:left">
    <svg class="crown" style="color:var(--gold);top:8px"><use href="#i-crown"/></svg>
    <div style="font-size:8px;font-weight:500;padding:10px 11px">Overall Statistics</div>
    <div class="tiles" style="bottom:5px">
      <div class="tile"><svg><use href="#i-history"/></svg><span style="line-height:1">Total Time</span><b>22 Min</b></div>
      <div class="tile"><svg><use href="#i-chev"/></svg><span style="line-height:1">Pace</span><b>8'48" /km</b></div>
      <div class="tile"><svg><use href="#i-cup"/></svg><span style="line-height:1">Calories</span><b>186 kcal</b></div>
    </div>
  </div>
  <div class="section" style="font-size:8px;font-weight:500;padding:12px 24px 6px">Ongoing Challenge</div>
  <div class="challenge">
    <span class="pill">Active</span>
    <h3>100km Challenge</h3>
    <div class="sub">12 days remaining</div>
    <div class="progress-row"><span>35.8 km completed</span><span>53%</span></div>
    <div class="bar"><i></i></div>
    <div class="prize"><svg><use href="#i-medal"/></svg><span>Prize Pool</span><b>US. 10,000</b></div>
  </div>
  <div style="height:20px"></div>
  <div class="history"><b>50km Speed Run</b><small>▦ Oct 2023</small><small>Completed · 2nd Place</small><svg class="medal" style="color:var(--gold)"><use href="#i-medal"/></svg><svg class="chev"><use href="#i-chev"/></svg></div>
  <div class="history"><b>Marathon Prep</b><small>▦ Sep 2023</small><small>Completed · Participation</small><svg class="medal"><use href="#i-medal"/></svg><svg class="chev"><use href="#i-chev"/></svg></div>
  <div class="history"><b>Summer Run</b><small>▦ Aug 2023</small><svg class="medal" style="color:var(--red)"><use href="#i-medal"/></svg></div>
  <nav class="nav"><svg><use href="#i-home"/></svg><svg class="on"><use href="#i-trophy"/></svg><svg><use href="#i-history"/></svg><svg><use href="#i-user"/></svg></nav>
</section>

<!-- Challenge details / join -->
<section class="screen s-join">
  <header class="topbar"><svg class="back"><use href="#i-back"/></svg><span>Overall Statistics</span><span class="join-btn">Join Challenge</span></header>
  <div class="hero" style="margin-top:11px">
    <span class="active-tag">Active Challenge</span>
    <svg class="runner"><use href="#i-runner"/></svg>
    <div class="big">100 km</div>
    <div class="label" style="letter-spacing:2.6px">Challenge</div>
    <div class="tiles">
      <div class="tile"><svg><use href="#i-user"/></svg><span style="line-height:1">Players</span><b>2,458</b></div>
      <div class="tile"><svg><use href="#i-history"/></svg><span style="line-height:1">Days Left</span><b>12</b></div>
      <div class="tile"><svg><use href="#i-trophy"/></svg><span style="line-height:1">Prize</span><b>$10,000</b></div>
    </div>
  </div>
  <div class="progress-card">
    <h3>Your Progress</h3>
    <div class="progress-row" style="margin-top:8px"><span>35.8 km completed</span><span>53%</span></div>
    <div class="bar"><i></i></div>
    <div class="metrics"><div>Time<br><b>48.5h</b></div><div>Speed<br><b>8.5km/h</b></div><div>Rank<br><b>#234</b></div></div>
  </div>
  <div class="rules">
    <div class="rule"><svg><use href="#i-chev"/></svg><div><b>Complete 100km</b><small>Complete 100km Within challenge period</small></div></div>
    <div class="rule"><svg><use href="#i-cal"/></svg><div><b>30 Days Timeline</b><small>Ends Dec 20, 2024</small></div></div>
    <div class="rule"><svg><use href="#i-history"/></svg><div><b>Minimum 2km per run</b><small>Each activity must qualify</small></div></div>
  </div>
  <div class="place"><svg class="medal" style="color:var(--gold)"><use href="#i-medal"/></svg><span>1st Place</span><b>$5,000</b></div>
  <nav class="nav"><svg><use href="#i-home"/></svg><svg class="on"><use href="#i-trophy"/></svg><svg><use href="#i-history"/></svg><svg><use href="#i-user"/></svg></nav>
</section>

<!-- Admin: create challenge -->
<section class="screen s-create">
  <header class="topbar"><svg class="back"><use href="#i-back"/></svg><span>Create Challenge</span></header>
  <div class="form">
    <label>Your Progress</label>
    <div class="input">ex 108 km Challenge</div>
    <label>Description</label>
    <div class="input area">Description your Challenge</div>
    <label>Upload Banner</label>
    <div class="upload"><b>Click to upload banner image</b><small>Recommended: 1200 x 400px</small></div>
    <label>Challenge Duration</label>
    <div class="input">Start Date / End Date</div>
    <label>Challenge Rules</label>
    <div class="input">Enter Rule<svg class="trash"><use href="#i-trash"/></svg></div>
    <div class="add-rule">+ &nbsp;Add Rule</div>
  </div>
  <div class="primary">Publish Challenge</div>
</section>

<!-- Sign up -->
<section class="screen s-signup">
  <div class="photo" role="img" aria-label="Photo of a runner's legs and shoes on an open desert road"></div>
  <div class="signup-head">
    <h2>Create Account</h2>
    <p>Join our running community and start tracking your progress</p>
  </div>
  <div class="form">
    <label>First Name</label>
    <div class="input">Tom</div>
    <label>Last Name</label>
    <div class="input">Calder</div>
    <label>Email</label>
    <div class="input">tm@runmail.test</div>
    <label>Password</label>
    <div class="input">tm@runmail.test</div>
  </div>
  <div class="primary">Signuo</div>
</section>

</body>
</html>
```